Tincture Design for Woman Owned CBD Branf

LumiVera is a luxery CBD brand for millennial women.

Our premium L Oil contains 500mg of full spectrum CBD derived from specially-sourced hemp for unparalleled purity and quality. Each dropper delivers approximately 20mg of CBD. Available in two flavors, Natural and Mint.

The goal is to design an aesthetically pleasing tincture (bottle dropper) with label and box. The final design should coincide with our brand guidelines and easily marketed for beauty consumers. We are looking for a clean design, the use of raised fonts and/or metallic is fine.

We have 4 other designs we'd like to work on with the winning designer.

Target Market(s)

Millennial Women, Income $75k+

Font styles to use
Other font styles liked:
• See Branding Sheet

Requirements
Must have
• Must follow brand guidelines (see attached for colors, font, etc)
Nice to have
• Raised font or Metallic Print

```html
<!DOCTYPE html>
<html lang="en">
<head>
<meta charset="utf-8">
<title>LumiVera L Oil – Tincture Label and Box</title>
<link href="https://fonts.googleapis.com/css2?family=Cinzel:wght@400&family=Source+Serif+4:wght@400;700&display=swap" rel="stylesheet">
<style>
  :root {
    --bg: #e4e5ea;
    --green: #24614f;
    --green-dark: #1c4e40;
    --white: #ffffff;
    --paper: #f6f6f6;
    --ink: #2b2f2d;
    --gold: #b9a77a;
  }
  * { margin: 0; padding: 0; box-sizing: border-box; }
  html, body { width: 1200px; height: 900px; overflow: hidden; background: var(--bg); }
  .canvas { position: relative; width: 1200px; height: 900px; }

  /* Bottle label */
  .label {
    position: absolute; left: 380px; top: 400px; width: 200px; height: 240px;
    background: var(--white); box-shadow: 0 2px 10px rgba(0,0,0,.06);
  }
  .label-name {
    position: absolute; top: 50px; width: 100%; text-align: center;
    font-family: "Cinzel", serif; font-size: 27px; color: var(--green); letter-spacing: 1px;
  }
  .label-tagline {
    position: absolute; top: 88px; width: 100%; text-align: center;
    font-family: "Source Serif 4", serif; font-size: 5.5px; letter-spacing: 2.5px; color: var(--gold);
  }
  .label-band {
    position: absolute; top: 110px; left: 0; width: 100%; height: 112px;
    background: var(--green); border-top: 3px solid var(--white); outline: 1px solid var(--green); outline-offset: 2px;
  }
  .label-banner {
    position: absolute; left: 50%; transform: translateX(-50%); top: -4px;
    width: 74px; height: 54px; border: 1.5px solid var(--white); border-top: none;
    text-align: center; color: var(--white); font-family: "Source Serif 4", serif;
  }
  .label-product { font-size: 24px; line-height: 28px; margin-top: 4px; }
  .label-cbd { font-size: 13px; line-height: 14px; letter-spacing: 1px; }
  .label-dot { display: block; margin: 5px auto 0; width: 5px; height: 5px; border-radius: 50%; background: var(--gold); }
  .label-flavor, .label-weight {
    position: absolute; width: 100%; text-align: center; color: var(--white);
    font-family: "Source Serif 4", serif; font-size: 15px; letter-spacing: 1px;
  }
  .label-flavor { top: 70px; }
  .label-weight { top: 88px; }

  /* Box */
  .box-front, .box-side { position: absolute; top: 150px; height: 540px; }
  .box-front { left: 620px; width: 170px; background: var(--paper); }
  .box-side  { left: 790px; width: 104px; background: #efefef; }
  .box-cap { height: 128px; display: flex; align-items: center; justify-content: center; }
  .box-front .box-cap { background: var(--green); }
  .box-side .box-cap  { background: var(--green-dark); }
  .box-mark { font-family: "Cinzel", serif; color: var(--white); font-size: 17px; letter-spacing: 1px; }
  .box-side .box-mark { font-size: 12px; }
  .box-rule { height: 6px; margin-top: 6px; }
  .box-front .box-rule { background: var(--green); }
  .box-side .box-rule { background: var(--green-dark); }

  .box-headline {
    margin: 36px 0 0 22px; width: 140px;
    font-family: "Source Serif 4", serif; font-weight: 700; font-size: 16px; line-height: 21px; color: var(--ink);
  }
  .box-headline .accent { color: var(--green); }
  .box-bar { height: 6px; background: var(--green-dark); }
  .box-front .box-bar { width: 68px; margin-left: 22px; }
  .box-use {
    margin: 8px 0 10px 22px; font-family: "Source Serif 4", serif; font-weight: 700;
    font-size: 12px; line-height: 15px; color: var(--ink);
  }
  .box-copy {
    margin: 20px 10px 0 10px; font-family: "Source Serif 4", serif;
    font-size: 9px; line-height: 12.5px; color: var(--ink);
  }
  .box-copy p { margin-bottom: 12px; }
  .box-side .box-bar { width: 84px; margin: 4px 10px 0; height: 7px; background: var(--green); }
</style>
</head>
<body>
<main class="canvas">

  <section class="label" aria-label="Bottle label">
    <h1 class="label-name">LumiVera</h1>
    <p class="label-tagline">PREMIUM CBD PRODUCTS</p>
    <div class="label-band">
      <div class="label-banner">
        <div class="label-product">L Oil</div>
        <div class="label-cbd">CBD</div>
        <span class="label-dot"></span>
      </div>
      <div class="label-flavor">Natural</div>
      <div class="label-weight">20g</div>
    </div>
  </section>

  <section class="box-front" aria-label="Box front panel">
    <div class="box-cap"><span class="box-mark">LumiVera</span></div>
    <div class="box-rule"></div>
    <h2 class="box-headline">Specially-sourced <span class="accent">hemp for</span> unparalleled purity and quality.</h2>
    <div style="height:96px"></div>
    <div class="box-bar"></div>
    <p class="box-use">For private<br>and commercial<br>purposes</p>
    <div class="box-bar"></div>
  </section>

  <section class="box-side" aria-label="Box side panel">
    <div class="box-cap"><span class="box-mark">LumiVera</span></div>
    <div class="box-rule"></div>
    <div class="box-copy">
      <p>Lorem ipsum dolor sit amet, consectetur adipiscing elit.</p>
      <p>Phasellus sed diam tincidunt lorem vulputate elementum.</p>
      <p>Mauris non risus bibendum, vestibulum augue eu, consequat ligula. Nam vel porta dui. Nam ut nisi id ex volutpat rhoncus. Proin dignissim, tortor in sagittis pulvinar, purus nulla faucibus diam, quis commodo augue sapien ultricies nulla.</p>
    </div>
    <div class="box-bar"></div>
  </section>

</main>
</body>
</html>
```